Hollister Brandt Law: Stationary
Professional
1st card: Gregory L. Marsh, 2nd card: Douglas Hollister, Esq.
Attorney
417 NW Palmetto Avenue Suite 220-B Stuart, FL 34996
greg@hollisterandmarsh.example
www.hollisterandmarsh.example
We are a 2 attorney firm. So, we need a card for each. The email for Douglas Hollister, Esq. is douglas@hollisterandmarsh.example. We need to have listed our other offices besides Stuart: Cedar Landing (561-555-0147), Ashford Point (772-555-0193), Kellan Shores (954-555-0128). I am not sure where to list these additional numbers and offices. On the stationary paper, we should have both attorneys names with our e-mails. I would like to see some designs with the address and telephone up top and also on the bottom. The stationary has to look professional as judges read these - so no need to have large swirls of color at the top or watermarkes. We also need a sign for our glass door with our logo, website, tel# 772-555-0165, and our practice areas: personal injury, medical malpractice, motor vehicle accidents, criminal defense, DUI defense, probation violations, admiralty & maritime below somewhere. If also a rolodex card, we would appreciate. I will upload the logo that we just got from brandmark bazaar.
I am not sure - I would like to see some suggestions. Maybe our office locations or: Personal Injury and Criminal Defense Trial Attorneys

```html
<!DOCTYPE html>
<html lang="en">
<head>
<meta charset="utf-8">
<title>Hollister Brandt Law — Stationery</title>
<link rel="stylesheet" href="https://fonts.googleapis.com/css2?family=Cinzel:wght@600&family=Cormorant+Garamond:wght@400;600&display=swap">
<style>
:root{
  --paper:#ffffff;
  --bg:#ffffff;
  --navy:#0c2a55;
  --gold:#a48a55;
  --name:#6a4a35;
  --muted:#77726c;
  --shadow:rgba(0,0,0,.14);
}
*{box-sizing:border-box;margin:0;padding:0}
html,body{width:1200px;height:883px;overflow:hidden;background:var(--bg)}
body{position:relative;font-family:"Cormorant Garamond",Georgia,serif;color:var(--muted)}
.sheet{position:absolute;background:var(--paper);box-shadow:0 1px 4px var(--shadow)}
.brand{display:flex;align-items:center;gap:6px;justify-content:center}
.brand-dot{border-radius:50%;background:var(--navy);flex:none}
.brand-name{font-family:"Cinzel",Georgia,serif;font-weight:600;color:var(--navy);letter-spacing:.03em;white-space:nowrap}

/* letterhead */
.letterhead{left:324px;top:29px;width:468px;height:823px}
.letterhead .brand{margin-top:44px}
.letterhead .brand-dot{width:22px;height:22px}
.letterhead .brand-name{font-size:16px}
.letterhead-foot{position:absolute;left:0;right:0;top:782px;text-align:center;font-size:7.5px;line-height:12px}

/* envelope */
.envelope{left:24px;top:312px;width:739px;height:328px;border-bottom:5px solid var(--gold)}
.envelope .flap{position:absolute;left:0;top:-84px;width:739px;height:84px}
.envelope .brand{position:absolute;left:0;width:624px;top:84px}
.envelope .brand-dot{width:24px;height:24px}
.envelope .brand-name{font-size:18px}
.window{position:absolute;left:379px;top:151px;width:209px;height:108px;border-radius:6px;background:linear-gradient(180deg,#f4f4f4,#dcdcdc);border:1px solid #d2d2d2}
.return-address{position:absolute;left:0;width:624px;top:302px;text-align:center;font-size:7.5px}

/* cards */
.card{left:931px;width:209px}
.card-front{border-bottom:4px solid var(--gold);text-align:center}
.card-name{margin-top:8px;font-size:9.5px;font-weight:600;color:var(--name);line-height:12px}
.card-title{font-size:6px;line-height:8px;margin-bottom:8px}
.card-front .brand-dot{width:14px;height:14px}
.card-front .brand-name{font-size:10px}
.card-details{margin-top:8px;font-size:5px;line-height:7px}
.card-back svg{display:block}
.card-1{top:29px;height:139px}
.card-2{top:180px;height:139px}
.card-3{top:336px;height:134px}
.card-4{top:487px;height:137px}
</style>
</head>
<body>

<section class="sheet letterhead" aria-label="Letterhead">
  <div class="brand"><span class="brand-dot"></span><span class="brand-name">Hollister Brandt Law</span></div>
  <div class="letterhead-foot">
    <p>417 NW Palmetto Avenue Suite 220-B Marlow Bay, FL 30918 · P: 555-010-0165</p>
    <p>Douglas Hollister, Esq. douglas@hollisterandmarsh.example · Gregory L. Marsh greg@hollisterandmarsh.example</p>
  </div>
</section>

<section class="sheet envelope" aria-label="Envelope">
  <svg class="flap" viewBox="0 0 739 84" preserveAspectRatio="none" aria-hidden="true">
    <defs>
      <linearGradient id="flapFill" x1="0" y1="0" x2="0" y2="1">
        <stop offset="0" stop-color="#0a2550"/><stop offset="1" stop-color="#24568f"/>
      </linearGradient>
    </defs>
    <path d="M0 84 C170 60 230 0 340 0 C450 0 540 50 739 84 Z" fill="url(#flapFill)"/>
    <circle cx="340" cy="30" r="8" fill="#ffffff"/>
  </svg>
  <div class="brand"><span class="brand-dot"></span><span class="brand-name">Hollister Brandt Law</span></div>
  <div class="window"></div>
  <p class="return-address">417 NW Palmetto Avenue Suite 220-B Marlow Bay, FL 30918</p>
</section>

<section class="sheet card card-front card-1" aria-label="Business card front, Gregory L. Marsh">
  <p class="card-name">Gregory L. Marsh</p>
  <p class="card-title">Attorney</p>
  <div class="brand"><span class="brand-dot"></span><span class="brand-name">Hollister Brandt Law</span></div>
  <div class="card-details">
    <p>417 NW Palmetto Avenue Suite 220-B Marlow Bay, FL 30918</p>
    <p>Cedar Landing 555-010-0147 · Ashford Point 555-010-0193 · Kellan Shores 555-010-0128</p>
    <p>greg@hollisterandmarsh.example · www.hollisterandmarsh.example</p>
  </div>
</section>

<section class="sheet card card-back card-2" aria-label="Business card back">
  <svg width="209" height="139" viewBox="0 0 209 139" aria-hidden="true">
    <defs>
      <radialGradient id="backFill" cx=".5" cy=".5" r=".7">
        <stop offset="0" stop-color="#2a64a6"/><stop offset="1" stop-color="#061733"/>
      </radialGradient>
    </defs>
    <rect width="209" height="139" fill="url(#backFill)"/>
    <circle cx="104.5" cy="69.5" r="10" fill="#ffffff"/>
  </svg>
</section>

<section class="sheet card card-front card-3" aria-label="Business card front, Douglas Hollister, Esq.">
  <p class="card-name">Douglas Hollister, Esq.</p>
  <p class="card-title">Attorney</p>
  <div class="brand"><span class="brand-dot"></span><span class="brand-name">Hollister Brandt Law</span></div>
  <div class="card-details">
    <p>417 NW Palmetto Avenue Suite 220-B Marlow Bay, FL 30918</p>
    <p>Cedar Landing 555-010-0147 · Ashford Point 555-010-0193 · Kellan Shores 555-010-0128</p>
    <p>douglas@hollisterandmarsh.example · www.hollisterandmarsh.example</p>
  </div>
</section>

<section class="sheet card card-back card-4" aria-label="Business card back">
  <svg width="209" height="137" viewBox="0 0 209 137" aria-hidden="true">
    <rect width="209" height="137" fill="url(#backFill)"/>
    <circle cx="104.5" cy="68.5" r="10" fill="#ffffff"/>
  </svg>
</section>

</body>
</html>
```